Wix Website

I would like to migrate my current website (www.tallowbrookhub.com) over to a Wix template. Right now, I think my site is too playful. I am looking for a really clean, modern and updated feel. I still want a classical feel. Simple the better. As for what we do, we are a provider of in-home tutoring. We service young to old. students alike. Looking for something academic but not pre-school. A good balance of elementary to high school.

Looking also to scale down the site to as little pages as possible. Again, simple the better. Would like a really good home page and an even better landing page that highlights a quick and easy signup form.

Please feel free to get as much info off the current site to make the page. The final design should highlight "The Human Side of Tutoring". Please make sure our tagline of "Helping students and their parents live above the stress and strain of academic struggles" is prominent. Appropriate Stock photos are permissible at this time. We can change them as needed

```html
<!DOCTYPE html>
<html lang="en">
<head>
<meta charset="utf-8">
<title>Tallowbrook Hub – In-Home Tutoring</title>
<link href="https://fonts.googleapis.com/css2?family=Arimo:wght@400;700&family=Open+Sans:wght@400;600&family=Oswald:wght@500&display=swap" rel="stylesheet">
<style>
:root{
  --bg:#f6de92;
  --page:#fbf8ee;
  --red:#c9163b;
  --red-dark:#b3102f;
  --orange:#c8621c;
  --ink:#2f2f2f;
  --body:#4a4a4a;
  --card:#ffffff;
  --line:#8a8a8a;
}
*{box-sizing:border-box;margin:0;padding:0}
html,body{width:1053px;height:1200px;overflow:hidden}
body{background:var(--bg);font-family:"Open Sans",sans-serif;color:var(--body);position:relative}
.page{position:absolute;left:151px;top:0;width:751px;height:1200px;background:var(--page)}
.abs{position:absolute}
.brand{left:10px;top:28px;display:flex;align-items:center;gap:8px;font-family:"Arimo",sans-serif;font-weight:700;font-size:26px;color:var(--red);letter-spacing:.5px}
.brand-dot{width:18px;height:18px;border-radius:50%;background:var(--orange)}
.top-nav{right:8px;top:34px;display:flex;gap:33px;font-family:"Arimo",sans-serif;font-size:10.5px;color:var(--ink)}
.call{right:8px;top:62px;font-family:"Arimo",sans-serif;font-size:14px;color:var(--ink);display:flex;align-items:baseline;gap:5px}
.call strong{font-family:"Oswald",sans-serif;font-weight:500;font-size:20px;color:var(--red)}
.main-nav{left:7px;top:97px;width:736px;height:43px;background:linear-gradient(#d81f44,var(--red-dark));border-radius:3px;box-shadow:0 2px 0 #8e0d26;display:flex;align-items:center;font-family:"Arimo",sans-serif;font-size:10.5px;color:#fff}
.main-nav a{color:#fff;text-decoration:none;padding:0 19px;height:100%;display:flex;align-items:center}
.main-nav a.active{background:linear-gradient(#d8732a,#b9561a);padding:0 27px;border-radius:3px 0 0 3px}
.hero{left:7px;top:146px;width:736px;height:320px;border-radius:3px;overflow:hidden;background:linear-gradient(160deg,#3d4a40 0%,#55604f 35%,#a97a5a 60%,#c49a7a 78%,#5f8fb0 100%);box-shadow:0 1px 2px rgba(0,0,0,.3)}
.hero-arrow{top:150px}
.hero-caption{left:80px;top:257px;width:577px;height:45px;background:rgba(255,255,255,.82);border-radius:3px;display:flex;align-items:center;justify-content:center;font-family:"Arimo",sans-serif;font-size:14px;color:var(--ink)}
.welcome{left:7px;top:492px;width:736px;height:146px;background:var(--card);border-radius:3px;box-shadow:0 2px 0 var(--line);text-align:center;padding-top:20px}
.welcome h1{font-family:"Arimo",sans-serif;font-weight:400;font-size:19px;color:var(--red)}
.welcome h1 span{color:#6b1a22}
.welcome h2{font-family:"Arimo",sans-serif;font-weight:400;font-size:13.5px;color:var(--orange);margin-top:6px}
.welcome p{font-size:10px;line-height:16.5px;margin:9px 26px 0}
.card{top:658px;width:234px;height:275px;background:var(--card);border-radius:3px;box-shadow:0 2px 0 var(--line);padding:16px 12px 0}
.card h3{font-family:"Arimo",sans-serif;font-weight:400;font-size:14px;color:var(--red)}
.card .photo{width:208px;height:98px;border-radius:3px;margin-top:12px}
.card p{font-size:10px;line-height:16.5px;margin-top:11px;padding-left:2px}
.signup{left:7px;top:958px;width:736px;height:168px;background:linear-gradient(#d71f43,#c0102f);border-radius:3px;box-shadow:0 2px 0 #8a8a8a}
.signup h4{position:absolute;top:21px;width:100%;text-align:center;font-family:"Arimo",sans-serif;font-weight:400;font-size:14px;color:#fff}
.field{top:51px;width:221px;height:35px;border:1px solid #fff;border-radius:3px;color:#fff;font-family:"Arimo",sans-serif;font-size:11px;display:flex;align-items:center;padding-left:15px}
.submit{left:311px;top:109px;width:114px;height:35px;background:linear-gradient(#d6702a,#b9561a);border-radius:3px;box-shadow:0 2px 0 #7a3610;color:#fff;font-family:"Arimo",sans-serif;font-size:11px;display:flex;align-items:center;justify-content:center}
.footer{left:7px;top:1163px;font-size:10px;color:var(--ink)}
.social{right:9px;top:1161px;display:flex;gap:5px}
.social span{width:18px;height:18px;border-radius:50%;background:#a9a9a9}
</style>
</head>
<body>
<div class="page">
  <div class="abs brand"><span class="brand-dot"></span>Tallowbrook Hub</div>
  <nav class="abs top-nav"><span>WHAT</span><span>WHY</span><span>WHO</span><span>HOW</span><span>LET'S GO</span></nav>
  <div class="abs call">CALL US : <strong>555.014.2290</strong></div>

  <nav class="abs main-nav">
    <a class="active">HOME</a><a>OUR STORY</a><a>OUR TUTORING</a><a>FAQ</a><a>AREAS WE SERVE</a><a>CONTACT US</a><a>SUMMER TUTORING</a>
  </nav>

  <div class="abs hero" role="img" aria-label="Smiling schoolchildren raising their hands in a classroom">
    <svg class="abs hero-arrow" style="left:16px" width="20" height="20" viewBox="0 0 20 20"><circle cx="10" cy="10" r="10" fill="rgba(0,0,0,.45)"/><path d="M11.5 6 7.5 10l4 4" stroke="#bbb" stroke-width="1.6" fill="none"/></svg>
    <svg class="abs hero-arrow" style="right:16px" width="20" height="20" viewBox="0 0 20 20"><circle cx="10" cy="10" r="10" fill="rgba(0,0,0,.45)"/><path d="M8.5 6l4 4-4 4" stroke="#bbb" stroke-width="1.6" fill="none"/></svg>
    <div class="abs hero-caption">Helping students and their parents live above the stress and strain of academic struggles</div>
  </div>

  <section class="abs welcome">
    <h1>WELCOME TO TALLOWBROOK <span>HUB</span></h1>
    <h2>Helping students and their parents live above the stress and strain of academic struggles.</h2>
    <p>Ut wisi enim ad minim veniam, quis nostrud exerci tation ullamcorper suscipit lobortis nisl ut aliquip ex ea commodo consequat. Duis autem vel eum iriure dolor in hendrerit in vulputate velit esse molestie consequat, vel illum dolore eu feugiat nulla facilisis at vero eros et accumsan et iusto odio dignissim qui blandit praesent luptatum zzril delenit augue duis</p>
  </section>

  <article class="abs card" style="left:8px">
    <h3>GET HELP</h3>
    <div class="photo" role="img" aria-label="Tutor helping a boy with his writing" style="background:linear-gradient(120deg,#eef0f2,#9fb8d6 50%,#2f6fb8)"></div>
    <p>Is your child struggling in school and needs help that you can't provide? In home tutoring from Tallowbrook Hub provides the opportunity for academic excellence while helping your child build confidence through one on one learning.</p>
  </article>
  <article class="abs card" style="left:258px">
    <h3>GET BACK ON TRACK</h3>
    <div class="photo" role="img" aria-label="Young children sitting in a row in a classroom" style="background:linear-gradient(120deg,#c9b9a4,#b84a3c 40%,#3f8a55 70%,#6d6457)"></div>
    <p>Getting back on track is easy when your struggling student is matched with the ideal tutor that meets their needs. Our tutors are not only passionate about their areas of expertise but they are passionate about your child's success.</p>
  </article>
  <article class="abs card" style="left:509px">
    <h3>GET RESULTS</h3>
    <div class="photo" role="img" aria-label="Students in blue uniforms writing at their desks" style="background:linear-gradient(120deg,#d9c7a0,#8b7b62 40%,#27429a 75%,#5a83b8)"></div>
    <p>Through the assistance tutoring provides, your child will get results. You will see not only academic improvements, but also increased confidence and peace of mind. Let Tallowbrook Hub help your child soar!</p>
  </article>

  <section class="abs signup">
    <h4>SIGNUP NOW</h4>
    <div class="abs field" style="left:17px">NAME</div>
    <div class="abs field" style="left:257px">EMAIL ADDRESS</div>
    <div class="abs field" style="left:498px">PHONE</div>
    <div class="abs submit">SUBMIT</div>
  </section>

  <footer class="abs footer">Tallowbrookhub © 2014. All Right Reserved.</footer>
  <div class="abs social" aria-label="Social links"><span></span><span></span><span></span><span></span><span></span><span></span></div>
</div>
</body>
</html>
```